" SOU MÉDICO ORTOPEDISTA COM ESPECIALIZAÇÃO EM CIRURGIA DO JOELHO E DO QUADRIL. REALIZO ATENDIMENTOS AMBULATORIAIS E CIRURGICOS NESTAS ARÉAS PRINCIPALMENTE. "

```html
<!DOCTYPE html>
<html lang="pt-BR">
<head>
<meta charset="utf-8">
<title>Marcelo Tavares Brandão — Pasta</title>
<link href="https://fonts.googleapis.com/css2?family=Montserrat:wght@300;400;500&display=swap" rel="stylesheet">
<style>
  :root {
    --backdrop: #ecebe8;
    --paper: #ffffff;
    --navy-deep: #0b2440;
    --navy: #123c5e;
    --navy-light: #1a5478;
    --blue-bright: #2fa6de;
    --blue-mid: #1f74bd;
    --ink-grey: #8a98a6;
    --ink-blue: #3c82b8;
    --text-light: #dbe8f2;
  }
  * { margin: 0; padding: 0; box-sizing: border-box; }
  html, body {
    width: 1200px; height: 1200px; overflow: hidden;
    background: var(--backdrop);
    font-family: "Montserrat", sans-serif;
  }
  .folder {
    position: absolute; left: 180px; top: 240px;
    width: 848px; height: 720px;
    display: flex;
    box-shadow: 0 20px 40px rgba(0,0,0,0.18);
  }
  .panel { position: relative; width: 424px; height: 720px; overflow: hidden; }
  .panel--inside { background: var(--paper); }
  .panel--cover {
    background: linear-gradient(90deg, var(--navy-deep) 0%, var(--navy) 55%, var(--navy-light) 100%);
  }
  .identity {
    position: absolute; left: 0; right: 0; top: 250px;
    display: flex; flex-direction: column; align-items: center;
  }
  .identity__mark {
    width: 40px; height: 40px; border-radius: 50%;
    border: 2px solid var(--ink-blue); margin-bottom: 12px;
  }
  .identity__name {
    font-weight: 400; font-size: 17px; letter-spacing: 0.6px;
    color: var(--ink-grey); text-transform: uppercase; white-space: nowrap;
  }
  .identity__field {
    margin-top: 5px; font-weight: 400; font-size: 8.5px; letter-spacing: 3.2px;
    color: var(--ink-blue); text-transform: uppercase;
  }
  .panel--cover .identity__mark { border-color: var(--text-light); }
  .panel--cover .identity__name { color: var(--text-light); }
  .panel--cover .identity__field { color: #9fc6e2; }
  .pocket { position: absolute; left: 0; bottom: 0; width: 424px; height: 200px; }
  .pocket__contact {
    position: absolute; left: 24px; bottom: 66px;
    font-size: 8px; line-height: 13px; color: #eaf4fb; letter-spacing: 0.4px;
  }
</style>
</head>
<body>
  <main class="folder">
    <section class="panel panel--inside">
      <div class="identity">
        <span class="identity__mark"></span>
        <h1 class="identity__name">Marcelo Tavares Brandão</h1>
        <p class="identity__field">Ortopedia e Traumatologia</p>
      </div>
      <svg class="pocket" viewBox="0 0 424 200" aria-hidden="true">
        <defs>
          <linearGradient id="pocketFill" x1="0" y1="0" x2="1" y2="0">
            <stop offset="0" stop-color="#1a4f93"/>
            <stop offset="0.55" stop-color="#1f74bd"/>
            <stop offset="1" stop-color="#2fa6de"/>
          </linearGradient>
        </defs>
        <path d="M0 20 H330 C395 20 424 60 424 110 V200 H0 Z" fill="url(#pocketFill)"/>
        <path d="M330 20 C380 20 412 50 420 95 C405 150 385 180 330 200 L424 200 V110 C424 60 395 20 330 20 Z" fill="#2a9ad6" opacity="0.6"/>
        <path d="M0 20 H330" stroke="#0f3f78" stroke-width="2"/>
      </svg>
      <div class="pocket__contact">
        <p>Rua das Acácias, 120 - Sala 304</p>
        <p>São Paulo - SP</p>
        <p>contato@mtbrandao.com.br</p>
        <p>(11) 4000-0000</p>
      </div>
    </section>
    <section class="panel panel--cover">
      <div class="identity">
        <span class="identity__mark"></span>
        <h2 class="identity__name">Marcelo Tavares Brandão</h2>
        <p class="identity__field">Ortopedia e Traumatologia</p>
      </div>
    </section>
  </main>
</body>
</html>
```